Beautiful & Elegant Digital Brochure Needed For Luxury Real Estate Development

Hello,

Our company is seeking a beautiful design for our real estate development that is currently being launched.

About The Project:
Development Name - Willow Crest Estate
Location - Charleston, S.C.
Low-Country Southern Style Architecture
Google "low-country" Charleston, SC to get an idea of the unique culture of the city
Google "willow crest tree" Charleston, SC to understand the branding

Other Digital Brochures that we love

http://www.fernvalehotels.example/cedarhollow/wp-content/uploads/sites/6/2014/08/adventures-brochure.pdf

Why we like it... We love the classy feeling the brochure portrays by using unique fonts and backgrounds (burlap textures). We also love the images that represent a "low-country" vibe.

Requirements:
1. We will be providing all of the content (attached)

2. Please use plenty of southern low-country stock images from PixelVaultStock (we have a subscription so just use the watermarked images unless you have full permissions)

3. Do not copy the Cedar Hollow brochure - create a unique vision that fits in to the low-country and southern vibe

4. Attached is our logos

The font we like to use is - Caslon Antique / italic
Thank you!

Project Deadline Extended Reason: We've added more design information and we need to get more designers to participate. Added Monday, May 30, 2016

Target Market(s)

High net worth individuals - each homesite will be over 6 million dollars USD

Industry/Entity Type

Real Estate Development

Font styles to use
Script
Other font styles liked:
• Caslon Antique & Italic

Colors
abd036
00a990
acd036
9bcb3c
33b8a4
86cfc6
cfeae6

Requirements
Must have
• low country feeling
Nice to have
• burlap, wood backgrounds
Should not have
• Should NOT be corporate. This brochure is for multi-millionaire home buyers and investors. They are seeking simple, beautiful, quiet, serene, and southern lifestyles on the Intracoastal waterway on Marley Isle, Charleston, South Carolina.

```html
<!DOCTYPE html>
<html lang="en">
<head>
<meta charset="utf-8">
<title>Willow Crest Estate – Lowcountry Brochure Spreads</title>
<link rel="stylesheet" href="https://fonts.googleapis.com/css2?family=Libre+Caslon+Text:ital,wght@0,400;1,400&family=Parisienne&display=swap">
<style>
  :root {
    --backdrop: #e4e4e4;
    --paper: #ffffff;
    --ink: #2b2b2b;
    --ink-soft: #3a3a3a;
    --frame-gold: #c9a56a;
    --sky: #6f9fd6;
    --palm: #5f8a3a;
    --burlap: #8a5f36;
    --hops: #a9c64b;
    --harbor: #6e8a6a;
    --diner: #d9b98a;
  }
  * { box-sizing: border-box; margin: 0; padding: 0; }
  html, body { width: 1200px; height: 976px; overflow: hidden; }
  body { background: var(--backdrop); position: relative; font-family: "Libre Caslon Text", Georgia, serif; color: var(--ink); }

  .spread { position: absolute; left: 42px; width: 1132px; background: var(--paper); }
  .spread--weather { top: 34px; height: 438px; }
  .spread--attractions { top: 496px; height: 436px; }

  .photo { position: absolute; }
  .photo--framed { border: 2px solid var(--frame-gold); }

  .photo--battery { left: 0; top: 0; width: 568px; height: 438px;
    background: linear-gradient(180deg, #4f86cf 0%, #9cc0e6 45%, #c7b48e 62%, #6b8f45 80%, #3f6a2c 100%); }
  .photo--burlap { left: 0; top: 0; width: 198px; height: 436px;
    background: linear-gradient(100deg, #9bbe49 0%, #a9c64b 20%, #8a5f36 42%, #7a5330 100%); }
  .photo--dining { left: 234px; top: 118px; width: 291px; height: 141px;
    background: linear-gradient(90deg, #d8c8a8 0%, #e6d6b6 50%, #b7c07a 100%); }
  .photo--tugboats { left: 595px; top: 44px; width: 184px; height: 165px;
    background: linear-gradient(180deg, #4f6e44 0%, #7d9072 45%, #c24a36 62%, #8d9a94 100%); }
  .photo--pavilion { left: 595px; top: 222px; width: 184px; height: 166px;
    background: linear-gradient(180deg, #4a7fc8 0%, #9cc0e6 35%, #e1cf96 60%, #d9d0b8 100%); }

  .script-heading { font-family: "Parisienne", "Brush Script MT", cursive; font-weight: 400; font-size: 19px; color: var(--ink); line-height: 1.1; }
  .subhead { font-style: italic; font-size: 10.2px; font-weight: 400; color: var(--ink); }
  .lede { font-style: italic; font-size: 9.2px; line-height: 14.4px; color: var(--ink-soft); }
  .body-copy { font-size: 8.3px; line-height: 13.6px; text-align: justify; color: var(--ink-soft); }
  .body-copy + .body-copy { margin-top: 6px; }

  .weather-title { position: absolute; left: 600px; top: 186px; width: 200px; text-align: right; }
  .weather-title .lede { margin-top: 2px; }
  .weather-copy { position: absolute; left: 823px; top: 84px; width: 262px; }

  .attractions-intro { position: absolute; left: 234px; top: 32px; width: 298px; }
  .attractions-intro .lede { margin-top: 4px; }

  .feature { position: absolute; }
  .feature .subhead { margin-bottom: 6px; }
  .feature--cuisine { left: 234px; top: 278px; width: 293px; }
  .feature--marine { left: 808px; top: 48px; width: 271px; }
  .feature--art { left: 808px; top: 260px; width: 271px; }
</style>
</head>
<body>

<section class="spread spread--weather">
  <div class="photo photo--battery" role="img" aria-label="Waterfront promenade lined with palmettos, flowering oleanders and historic pastel mansions under a blue sky"></div>

  <header class="weather-title">
    <h2 class="script-heading">Let the Weather Draw You Out</h2>
    <p class="lede">Thanks to the beautiful vistas and exceptionally good weather, the Lowcountry is a mecca for outdoor living.</p>
  </header>

  <div class="weather-copy">
    <p class="body-copy">Because of Charleston's temperate climate, outdoor attractions are available year-round. The area boasts short, mild winters and long, hot summers. Measurable snowfall is rare, and the temperature rarely drops below freezing. Spring and fall are marked by comfortable, consistent temperatures that will coax you out of doors. Rich, well-draining soil and a consistent, temperate climate afford gardeners the luxury of a year round growing season and open the door to a wide array of landscaping options not readily enjoyed in many areas.</p>
    <p class="body-copy">For centuries, natives of the Lowcountry have designed their residences to take advantage of the region's enviable weather conditions and wind patterns. Large porches, sizable verandas and generous roof overhangs are conventional residential features allowing not only cover from the midday sun but also providing an ideal location to sip cocktails and entertain guests. Charlestonians relish the area's prevailing winds and their strong, cool breezes. These draft inland, sweeping through open air porches and wafting through open windows.</p>
  </div>
</section>

<section class="spread spread--attractions">
  <div class="photo photo--burlap" role="img" aria-label="Fresh green hops resting on a burlap texture"></div>

  <header class="attractions-intro">
    <h2 class="script-heading">Charleston's Attractions</h2>
    <p class="lede">Whatever your interests, the Lowcountry paradise has something for everyone. Charleston offers a multitude of unique attractions that simply must be seen.</p>
  </header>

  <div class="photo photo--framed photo--dining" role="img" aria-label="Family enjoying a meal together at a sunny restaurant table"></div>

  <article class="feature feature--cuisine">
    <h3 class="subhead">Culture Meets Cuisine</h3>
    <p class="body-copy">Visit some of Charleston's finest eateries and meet the culinary minds behind the masterpieces. Learn about the history and evolution of Lowcountry cuisine. Enjoy samples and unlock new skills. Charleston offers a wide range of culinary tours designed to expose inhabitants and visitors to some of the area's best fare. From wine pairing tours to excursions to find the city's best deserts, there is a tour for every flavor. For those new to the area, this is an excellent way to experience local cuisine and find the area's hidden gems.</p>
  </article>

  <div class="photo photo--framed photo--tugboats" role="img" aria-label="Two red and white tugboats moored at a wooded harbor"></div>
  <div class="photo photo--framed photo--pavilion" role="img" aria-label="Ornate seaside pavilion on a pier above a sandy beach"></div>

  <article class="feature feature--marine">
    <h3 class="subhead">Learn About Marine Life</h3>
    <p class="body-copy">The city's expansive aquarium offers visitors a chance to enjoy the beauty of marine life first-hand. Featuring more than 5000 indigenous and exotic species of fish, reptile, and amphibians, the aquarium invites the curious and adventurous alike. Interactive exhibits encourage visitors to get up close and personal with wildlife that is rarely seen and often misunderstood. Bonnethead and cownose sharks, southern stingrays, starfish, hermit crabs, and sea urchins reside in large tanks with shallow pools that are designed to allow visitors to reach out and touch the animals. Enthusiastic and knowledgeable volunteers are always nearby to guarantee safety and provide information and insight. The facility opens into the adjoining Charleston Harbor where bottlenose dolphins and sea turtles can be observed in an intimate setting few people have the pleasure of enjoying.</p>
  </article>

  <article class="feature feature--art">
    <h3 class="subhead">Art in the City</h3>
    <p class="body-copy">In recent decades, a powerful cultural initiative has taken root in the city. Folk art and artisan crafts remain integral elements of the Charleston art scene. Arts festivals and events occur year-round and the multitude of galleries featuring original works from local and world-renowned artists is ever-expanding. Fine art galleries as well as those housing contemporary or modern works are scattered throughout the city. Open air exhibits and outdoor statue gardens provide an alternative way to experience the local culture while keeping the arts accessible to the public.</p>
  </article>
</section>

</body>
</html>
```